Christmas Card for Holidays to Companies Clients

Hello designers! We are looking for the best Christmas Cards we can get to send out to our companies clients in the holidays. We don't have a lot of specifications, we just wanted to have a little detail with them for the upcoming holidays.

Our company is a technological company that offers different product, solutions and services. Most of our clients are some of the countries banks.

Colors

Designer to choose colors to be used in the design.

Requirements
Must have
• The logo and name of our company (Lumoventa) and a nice but short and precise message for the holidays.

```html
<!DOCTYPE html>
<html lang="en">
<head>
<meta charset="utf-8">
<title>Lumoventa Holiday Card</title>
<link rel="stylesheet" href="https://fonts.googleapis.com/css2?family=Yellowtail&family=Exo+2:wght@400;700&display=swap">
<style>
  :root {
    --page-bg: #e9e4dc;
    --card-dark: #262626;
    --frame-dark: #2d2d2d;
    --gold: #d8c9a4;
    --gold-deep: #b89a5c;
    --band-white: #f6f5f1;
    --brand-grey: #3a3a3a;
    --tagline-grey: #444444;
  }
  * { margin: 0; padding: 0; box-sizing: border-box; }
  html, body { width: 1200px; height: 800px; overflow: hidden; }
  body { background: var(--page-bg); position: relative; }

  .card {
    position: absolute; left: 240px; top: 40px;
    width: 720px; height: 720px;
    background: var(--card-dark);
    overflow: hidden;
    box-shadow: 0 10px 30px rgba(0,0,0,0.25);
  }
  .ornaments {
    position: absolute; top: 0; height: 597px; width: 130px;
  }
  .ornaments--left {
    left: 0;
    background:
      radial-gradient(circle at 95px 215px, #e8b84a 0 40px, transparent 42px),
      radial-gradient(circle at 55px 130px, #d9a943 0 35px, transparent 38px),
      radial-gradient(circle at 55px 320px, #a9a9a9 0 28px, transparent 30px),
      radial-gradient(circle at 30px 460px, #d4a540 0 38px, transparent 40px),
      linear-gradient(180deg, #2b2b2b, #1f1f1f);
  }
  .ornaments--right {
    right: 0; width: 110px;
    background:
      radial-gradient(circle at 70px 50px, #c9a14a 0 36px, transparent 38px),
      radial-gradient(circle at 70px 185px, #a5a5a5 0 28px, transparent 30px),
      radial-gradient(circle at 60px 365px, #e2b142 0 44px, transparent 46px),
      radial-gradient(circle at 75px 450px, #a8a8a8 0 28px, transparent 30px),
      radial-gradient(circle at 70px 560px, #d6a945 0 38px, transparent 40px),
      linear-gradient(180deg, #2b2b2b, #1f1f1f);
  }
  .ornaments--top {
    position: absolute; left: 100px; top: 0; width: 80px; height: 80px;
    background: radial-gradient(circle at 40px 28px, #b5b5b5 0 28px, transparent 30px);
  }

  .greeting-frame {
    position: absolute; left: 120px; top: 81px;
    width: 484px; height: 484px;
    background: var(--frame-dark);
    border: 3px solid var(--gold-deep);
    outline: 2px solid #6e6048;
    outline-offset: -9px;
    box-shadow: 0 4px 14px rgba(0,0,0,0.5), inset 0 0 0 6px #3a352c;
    display: flex; align-items: center; justify-content: center;
  }
  .greeting {
    font-family: "Yellowtail", cursive;
    color: var(--gold);
    font-size: 60px;
    line-height: 84px;
    text-align: center;
    font-weight: 400;
    margin-top: 8px;
  }

  .brand-band {
    position: absolute; left: 0; top: 597px;
    width: 720px; height: 98px;
    background: var(--band-white);
    display: flex; align-items: center; justify-content: center; gap: 18px;
  }
  .brand-mark {
    width: 60px; height: 60px; border-radius: 50%;
    background: #d7372b;
  }
  .brand-text { display: flex; flex-direction: column; }
  .brand-name {
    font-family: "Exo 2", sans-serif; font-weight: 700;
    font-size: 46px; line-height: 44px; letter-spacing: 0.5px;
    color: var(--brand-grey);
  }
  .brand-tagline {
    font-family: "Exo 2", sans-serif; font-weight: 400;
    font-size: 15px; letter-spacing: 1px;
    color: var(--tagline-grey); margin-top: 4px;
  }
</style>
</head>
<body>
  <main class="card">
    <div class="ornaments ornaments--left" role="img" aria-label="Gold stars, gold and silver glitter baubles and curled ribbon on black"></div>
    <div class="ornaments ornaments--top" role="img" aria-label="Silver glitter bauble"></div>
    <div class="ornaments ornaments--right" role="img" aria-label="Gold stars and gold and silver baubles on black"></div>

    <section class="greeting-frame">
      <p class="greeting">Wishing you a<br>very happy<br>Holiday season<br>and a wonderful<br>New Year!</p>
    </section>

    <footer class="brand-band">
      <span class="brand-mark"></span>
      <div class="brand-text">
        <span class="brand-name">LUMOVENTA</span>
        <span class="brand-tagline">IT CONSULTING AND SERVICES</span>
      </div>
    </footer>
  </main>
</body>
</html>
```